Design wine label. Brand name The Quillmere

Wine label design for 'The Quillmere'. A few varieties but example-

The Quillmere Shiraz 2016 Bendigo 750ml, 14%alc/vol.

'The quillmere' at top of label, image of sparrow then vintage, variety etc under image.

simple, yet striking and modern look.

Font styles to use
Script

Requirements
Must have
• Image of a sparrow
Nice to have
• Simple image, outline, cartoon or Lino print style. Some colour but not too busy

```html
<!DOCTYPE html>
<html lang="en">
<head>
<meta charset="utf-8">
<title>The Quillmere Shiraz – Label Series</title>
<link rel="stylesheet" href="https://fonts.googleapis.com/css2?family=Great+Vibes&family=Cinzel:wght@400;500&display=swap">
<style>
  :root {
    --backdrop: #8b8b8b;
    --silver-light: #f1f1f1;
    --silver-mid: #d9d9d9;
    --silver-dark: #b9b9b9;
    --frame: #3a3a3a;
    --ink: #1b1b1b;
    --crimson: #c8103e;
    --band: #161616;
    --band-text: #f2f2f2;
  }
  * { margin: 0; padding: 0; box-sizing: border-box; }
  html, body { width: 801px; height: 1200px; overflow: hidden; }
  body {
    background: var(--backdrop);
    display: flex;
    align-items: center;
    justify-content: center;
  }
  .label-series {
    display: flex;
    gap: 20px;
  }
  .label {
    position: relative;
    width: 240px;
    height: 314px;
    background: linear-gradient(100deg, var(--silver-dark) 0%, var(--silver-light) 30%, var(--silver-mid) 60%, var(--silver-light) 80%, var(--silver-dark) 100%);
    box-shadow: 0 2px 6px rgba(0,0,0,0.25);
  }
  .label__frame {
    position: absolute;
    inset: 7px;
    border: 1px solid var(--frame);
  }
  .label__title {
    position: absolute;
    top: 28px;
    left: 0; right: 0;
    text-align: center;
    font-family: "Great Vibes", cursive;
    font-size: 33px;
    color: var(--crimson);
    transform: rotate(-4deg);
    white-space: nowrap;
  }
  .label__artwork {
    position: absolute;
    top: 92px;
    left: 50%;
    width: 130px;
    height: 110px;
    transform: translateX(-50%);
  }
  .label__artwork svg { width: 100%; height: 100%; display: block; }
  .label__name {
    position: absolute;
    top: 228px;
    left: 0; right: 0;
    text-align: center;
    font-family: "Cinzel", serif;
    font-size: 12px;
    letter-spacing: 0.3px;
    color: var(--ink);
    white-space: nowrap;
  }
  .label__name .accent { color: var(--crimson); }
  .label__rule {
    position: absolute;
    top: 259px;
    left: 24px; right: 24px;
    height: 1px;
    background: #9a9a9a;
  }
  .label__details {
    position: absolute;
    top: 268px;
    left: 0; right: 0;
    text-align: center;
    font-family: "Cinzel", serif;
    font-size: 8.5px;
    color: var(--ink);
    white-space: nowrap;
  }
  .label__details .divider {
    display: inline-block;
    width: 1px;
    height: 11px;
    background: currentColor;
    vertical-align: middle;
    margin: 0 3px;
  }
  .label--banded .label__band {
    position: absolute;
    top: 218px;
    left: 9px; right: 9px;
    bottom: 9px;
    background: var(--band);
  }
  .label--banded .label__name,
  .label--banded .label__details { color: var(--band-text); }
  .label--banded .label__rule { background: #666; }
</style>
</head>
<body>
  <main class="label-series">

    <article class="label">
      <div class="label__frame"></div>
      <h1 class="label__title">The Quillmere</h1>
      <div class="label__artwork" role="img" aria-label="Black silhouette of a sparrow perched, facing right">
        <svg viewBox="0 0 130 110" preserveAspectRatio="none">
          <defs>
            <radialGradient id="art-silhouette" cx="50%" cy="50%" r="55%">
              <stop offset="0%" stop-color="#111" stop-opacity="0.75"/>
              <stop offset="100%" stop-color="#111" stop-opacity="0"/>
            </radialGradient>
          </defs>
          <rect width="130" height="110" fill="url(#art-silhouette)"/>
        </svg>
      </div>
      <p class="label__name">The <span class="accent">Quillmere</span> Shiraz</p>
      <div class="label__rule"></div>
      <p class="label__details">2016 Bendigo<span class="divider"></span>750mL / 14%alc/vol</p>
    </article>

    <article class="label label--banded">
      <div class="label__frame"></div>
      <div class="label__band"></div>
      <h1 class="label__title">The Quillmere</h1>
      <div class="label__artwork" role="img" aria-label="Engraved ink drawing of two sparrows perched together on a branch">
        <svg viewBox="0 0 130 110" preserveAspectRatio="none">
          <defs>
            <radialGradient id="art-pair" cx="50%" cy="50%" r="55%">
              <stop offset="0%" stop-color="#555" stop-opacity="0.6"/>
              <stop offset="100%" stop-color="#555" stop-opacity="0"/>
            </radialGradient>
          </defs>
          <rect width="130" height="110" fill="url(#art-pair)"/>
        </svg>
      </div>
      <p class="label__name">The <span class="accent">Quillmere</span> Shiraz</p>
      <div class="label__rule"></div>
      <p class="label__details">2016 Bendigo<span class="divider"></span>750mL / 14%alc/vol</p>
    </article>

    <article class="label">
      <div class="label__frame"></div>
      <h1 class="label__title">The Quillmere</h1>
      <div class="label__artwork" role="img" aria-label="Engraved ink drawing of a single sparrow perched on a twig">
        <svg viewBox="0 0 130 110" preserveAspectRatio="none">
          <defs>
            <radialGradient id="art-single" cx="50%" cy="50%" r="55%">
              <stop offset="0%" stop-color="#4a4a4a" stop-opacity="0.6"/>
              <stop offset="100%" stop-color="#4a4a4a" stop-opacity="0"/>
            </radialGradient>
          </defs>
          <rect width="130" height="110" fill="url(#art-single)"/>
        </svg>
      </div>
      <p class="label__name">The <span class="accent">Quillmere</span> Shiraz</p>
      <div class="label__rule"></div>
      <p class="label__details">2016 Bendigo<span class="divider"></span>750mL / 14%alc/vol</p>
    </article>

  </main>
</body>
</html>
```